3 banner themes for healthy foods supplements

Who you are
You are a top professional designer. You eat, sleep and breathe banners. You have them for breakfast, lunch and dinner. You have created so many high quality banners that you stopped counting.
Who we are
We are selling premium nutritional supplements.

Deliverables
We need to design 3 different banner themes, each in the following formats:
- Vertical rectangle: 240 x 400
- Mobile leaderboard: 320 x 50
- Banner: 468 x 60
- Leaderboard: 728 x 90
- Square: 250 x 250
- Small square: 200 x 200
- Large rectangle: 336 x 280
- Inline rectangle: 300 x 250
- Skyscraper: 120 x 600
- Wide skyscraper: 160 x 600
- Half-page: 300 x 600
- Large leaderboard: 970x90
- Large mobile banner: 320 x 100
- Billboard: 970 x 250
- Portrait: 300 x 1050

To give us a taste of your design skills, we invite you to submit one format (300 x 250) of each of the 3 different banner themes described below before we finally give you the green light and award you. Once awarded you should deliver all 3 themes with all above mentioned banner formats.

The final deliverable shall be editable .psd files.

Our products
The products we are advertising are organic, raw, vegan, premium nutritional supplements, such as algae powder, wheat grass powder and goji berries. The products stand to support a healthy life style. Please have a look at our shop. It is in German, but you get the gist. http://www.lumavera.-shop.example

The design
We would describe the style of the banners as follows:
- Premium
- Joyful
- White background
- Minimalistic

Each banner theme shall advertise the following messages about the products:
- Product name (chlorella algae powder , wheatgrass powder, goji berries)
- healthy
- 100 % vegan, raw and organic
- 100% natural
- premium product

Each of the above attributes can be represented with labels of different colours, similar to the attached sample files. We like the colour combination of the labels on this banner a lot.
All 3 themes shall contain our logo which you find attached to this job description. The logo shall be visible, but not too prominent.

The only difference between the 3 different themes shall be the product photo and the product name. All other elements on the banner shall be the same.

Theme A
This theme advertises algae powder, such as chlorella algae. The product photo is attached and should of course appear prominently on the banner.

Theme B
This theme advertises wheat grass powder. The product photo is attached and should of course appear prominently on the banner.

Theme C
This theme advertises goji berries. The product photo is attached and should of course appear prominently on the banner.

Target Market(s)

Health conscious people.

Industry/Entity Type

It Professional

Font styles to use
Sans Serif

Colors
00a990
a54499
f37122
fbed22
0692cd
9bcb3b
ffc214

Requirements
Must have
• - product image as per in the attachment
• - logo
• - bright, clear, joyful colors
Should not have
• - heavy dark colors
• - frame

```html
<!DOCTYPE html>
<html lang="en">
<head>
<meta charset="utf-8">
<title>Solvera – Superfood Banner Themes</title>
<link rel="stylesheet" href="https://fonts.googleapis.com/css2?family=Open+Sans:wght@400;600;700&display=swap">
<style>
  :root {
    --teal: #00a990;
    --purple: #a54499;
    --orange: #f37122;
    --yellow: #fbed22;
    --blue: #0692cd;
    --green: #9bcb3b;
    --gold: #ffc214;
    --white: #ffffff;
    --vegan-text: #1f7a3a;
    --button-text: #5b8a2a;
    --seal: #3c3c3c;

    --chlorella-sky: #1e9a55;
    --chlorella-label: rgba(28, 110, 70, 0.85);
    --chlorella-product: #3b5a3a;

    --wheat-sky: #9bcb3b;
    --wheat-label: rgba(130, 175, 50, 0.9);
    --wheat-product: #b8c47a;

    --goji-sky: #e8392c;
    --goji-label: rgba(230, 70, 55, 0.92);
    --goji-product: #d2392a;
  }

  * { box-sizing: border-box; margin: 0; padding: 0; }

  html, body {
    width: 1200px;
    height: 333px;
    overflow: hidden;
    background: var(--white);
    font-family: "Open Sans", Arial, sans-serif;
  }

  .symbol-library { position: absolute; width: 0; height: 0; }

  .banner-row {
    display: flex;
    width: 1200px;
    height: 333px;
  }

  .banner {
    position: relative;
    width: 400px;
    height: 333px;
    overflow: hidden;
    background: linear-gradient(180deg, var(--sky) 0%, color-mix(in srgb, var(--sky) 45%, white) 32%, var(--white) 62%);
  }

  .banner--chlorella { --sky: var(--chlorella-sky); --label: var(--chlorella-label); --product: var(--chlorella-product); }
  .banner--wheatgrass { --sky: var(--wheat-sky); --label: var(--wheat-label); --product: var(--wheat-product); }
  .banner--goji { --sky: var(--goji-sky); --label: var(--goji-label); --product: var(--goji-product); }

  .product-title {
    position: absolute;
    left: 13px;
    top: 11px;
    display: flex;
    flex-direction: column;
    align-items: flex-start;
    gap: 6px;
  }

  .product-title__line {
    display: block;
    background: var(--label);
    color: var(--white);
    font-size: 22px;
    font-weight: 400;
    letter-spacing: 0.5px;
    line-height: 1;
    padding: 3px 5px 3px 4px;
    text-transform: uppercase;
  }

  .shop-button {
    position: absolute;
    left: 267px;
    top: 27px;
    width: 94px;
    height: 23px;
    background: var(--yellow);
    color: var(--button-text);
    font-size: 13px;
    font-weight: 600;
    display: flex;
    align-items: center;
    justify-content: center;
    gap: 4px;
    border-radius: 2px;
    text-decoration: none;
  }

  .shop-button__chevron { font-weight: 700; font-size: 14px; }

  .product-photo {
    position: absolute;
    width: 170px;
    height: 80px;
    top: 80px;
    background: radial-gradient(ellipse at 50% 40%, color-mix(in srgb, var(--product) 85%, white) 0%, var(--product) 70%);
    border-radius: 50% 50% 46% 46% / 75% 75% 25% 25%;
  }

  .banner--chlorella .product-photo { left: 22px; }
  .banner--wheatgrass .product-photo { left: 70px; }
  .banner--goji .product-photo { left: 150px; width: 200px; top: 78px; }

  .claims {
    position: absolute;
    inset: 0;
    width: 400px;
    height: 333px;
  }

  .claim-text {
    font-family: "Open Sans", Arial, sans-serif;
    font-size: 20px;
    font-weight: 600;
    fill: var(--white);
  }

  .claim-text--vegan { fill: var(--vegan-text); }

  .brand-mark {
    position: absolute;
    right: 8px;
    bottom: 8px;
    display: flex;
    align-items: center;
    gap: 4px;
    color: var(--teal);
    font-size: 12px;
    font-weight: 600;
  }

  .brand-mark__dot {
    width: 9px;
    height: 9px;
    border-radius: 50%;
    background: var(--green);
  }
</style>
</head>
<body>
<svg class="symbol-library" aria-hidden="true">
  <symbol id="claim-ribbons" viewBox="0 0 400 333">
    <circle cx="37" cy="187" r="19" fill="var(--seal)" stroke="var(--gold)" stroke-width="3"/>
    <g transform="translate(200,220) rotate(-16)">
      <!-- raw and organic -->
      <polygon points="-60,-35 260,-35 260,-5 -60,-5 -48,-20" fill="var(--purple)"/>
      <text class="claim-text" x="54" y="-13" text-anchor="middle">raw and organic</text>
      <rect x="152" y="-32" width="24" height="24" fill="var(--white)"/>
      <path d="M156,-21 l6,7 l11,-15" stroke="var(--purple)" stroke-width="4" fill="none"/>

      <!-- 100 % Vegan -->
      <polygon points="-320,1 -84,1 -74,16 -84,31 -320,31" fill="var(--white)"/>
      <text class="claim-text claim-text--vegan" x="-150" y="23" text-anchor="middle">100 % Vegan</text>

      <!-- Natural -->
      <rect x="-70" y="1" width="165" height="30" fill="var(--orange)"/>
      <text class="claim-text" x="0" y="23" text-anchor="middle">Natural</text>
      <rect x="63" y="4" width="24" height="24" fill="var(--white)"/>
      <path d="M67,15 l6,7 l11,-15" stroke="var(--orange)" stroke-width="4" fill="none"/>

      <!-- 100 % -->
      <rect x="-320" y="35" width="262" height="30" fill="var(--orange)"/>
      <text class="claim-text" x="-120" y="57" text-anchor="middle">100 %</text>

      <!-- premium product -->
      <rect x="-40" y="31" width="300" height="30" fill="var(--blue)"/>
      <text class="claim-text" x="65" y="53" text-anchor="middle">premium product</text>
      <rect x="173" y="34" width="24" height="24" fill="var(--white)"/>
      <path d="M177,45 l6,7 l11,-15" stroke="var(--blue)" stroke-width="4" fill="none"/>

      <!-- healthy -->
      <rect x="-40" y="69" width="165" height="30" fill="var(--green)"/>
      <text class="claim-text" x="14" y="91" text-anchor="middle">healthy</text>
      <rect x="86" y="72" width="24" height="24" fill="var(--white)"/>
      <path d="M90,83 l6,7 l11,-15" stroke="var(--green)" stroke-width="4" fill="none"/>
    </g>
  </symbol>
</svg>

<main class="banner-row">

  <section class="banner banner--chlorella">
    <h2 class="product-title">
      <span class="product-title__line">Chlorella Algae</span>
      <span class="product-title__line">Powder</span>
    </h2>
    <a class="shop-button" href="http://www.lumavera.-shop.example">Shop Now <span class="shop-button__chevron">&rsaquo;</span></a>
    <div class="product-photo" role="img" aria-label="Heap of dark green chlorella algae powder"></div>
    <svg class="claims" viewBox="0 0 400 333" role="img" aria-label="raw and organic, 100 % Vegan, 100 % Natural, premium product, healthy"><use href="#claim-ribbons"/></svg>
    <div class="brand-mark"><span class="brand-mark__dot"></span>solvera</div>
  </section>

  <section class="banner banner--wheatgrass">
    <h2 class="product-title">
      <span class="product-title__line">Wheat Grass</span>
      <span class="product-title__line">Powder</span>
    </h2>
    <a class="shop-button" href="http://www.lumavera.-shop.example">Shop Now <span class="shop-button__chevron">&rsaquo;</span></a>
    <div class="product-photo" role="img" aria-label="Heap of pale green wheat grass powder"></div>
    <svg class="claims" viewBox="0 0 400 333" role="img" aria-label="raw and organic, 100 % Vegan, 100 % Natural, premium product, healthy"><use href="#claim-ribbons"/></svg>
    <div class="brand-mark"><span class="brand-mark__dot"></span>solvera</div>
  </section>

  <section class="banner banner--goji">
    <h2 class="product-title">
      <span class="product-title__line">Goji</span>
      <span class="product-title__line">Berries</span>
    </h2>
    <a class="shop-button" href="http://www.lumavera.-shop.example">Shop Now <span class="shop-button__chevron">&rsaquo;</span></a>
    <div class="product-photo" role="img" aria-label="Pile of dried red goji berries"></div>
    <svg class="claims" viewBox="0 0 400 333" role="img" aria-label="raw and organic, 100 % Vegan, 100 % Natural, premium product, healthy"><use href="#claim-ribbons"/></svg>
    <div class="brand-mark"><span class="brand-mark__dot"></span>solvera</div>
  </section>

</main>
</body>
</html>
```